Simple proffessional BC

I have a logo which I will attach below.
I would like the logo on the front of the card with these details in point form below:
Pre and Post Natal Yoga: Pregnancy Workshops: Hypnobirthing Courses
On the back of the card my details:
Marla Penrick
Facebook page- calmcradlestudiolakebay
Mobile- 0482 315 746

I like the idea of the card being simple, possibly just the above on a plain coloured (eggshell?) card, a card that is textured.
I am open to suggestion if it appeals!
Thank you and good luck!

Target Market(s)

Pregnant women, 20's-40's

Requirements
Must have
• Simple, compliment logo.
Make logo the feature.
Should not have

```html
<!DOCTYPE html>
<html lang="en">
<head>
<meta charset="utf-8">
<title>Calm Cradle – Business Card</title>
<link rel="stylesheet" href="https://fonts.googleapis.com/css2?family=Questrial&display=swap">
<style>
  :root {
    --page-bg: #ececec;
    --card-brown-dark: #8a3426;
    --card-brown-light: #c08a7a;
    --leaf-orange: #f0a33c;
    --leaf-stripe: rgba(255, 255, 255, 0.07);
    --ink-maroon: #7a1e1a;
    --badge-white: #ffffff;
    --ghost-circle: rgba(240, 163, 60, 0.35);
  }
  * { box-sizing: border-box; margin: 0; padding: 0; }
  html, body {
    width: 1200px;
    height: 900px;
    overflow: hidden;
    background: var(--page-bg);
    font-family: "Questrial", "Century Gothic", sans-serif;
    color: var(--ink-maroon);
  }
  .sheet {
    position: relative;
    width: 1200px;
    height: 900px;
  }
  .card {
    position: absolute;
    left: 270px;
    width: 660px;
    height: 377px;
    overflow: hidden;
    background: linear-gradient(90deg, var(--card-brown-light) 0%, var(--card-brown-dark) 28%, var(--card-brown-dark) 72%, var(--card-brown-light) 100%);
    box-shadow: 0 6px 18px rgba(0, 0, 0, 0.18);
  }
  .card--front { top: 50px; }
  .card--back { top: 473px; }
  .card__shape {
    position: absolute;
    inset: 0;
    width: 100%;
    height: 100%;
  }
  .leaf { fill: var(--leaf-orange); }
  .ghost-circle { fill: var(--ghost-circle); }

  .brand {
    position: absolute;
    left: 200px;
    top: 92px;
    display: flex;
    align-items: center;
    gap: 18px;
  }
  .brand__badge {
    width: 62px;
    height: 62px;
    border-radius: 50%;
    background: var(--badge-white);
  }
  .brand__name {
    font-size: 40px;
    color: var(--ink-maroon);
    letter-spacing: 0.5px;
  }
  .services {
    position: absolute;
    left: 150px;
    top: 208px;
    list-style: none;
    font-size: 21px;
    line-height: 1.5;
  }
  .services li::before {
    content: "•";
    margin-right: 10px;
  }

  .holder-name {
    position: absolute;
    right: 60px;
    top: 40px;
    font-size: 24px;
  }
  .contact {
    position: absolute;
    left: 190px;
    bottom: 40px;
    font-size: 21px;
    line-height: 1.75;
  }
</style>
</head>
<body>
<main class="sheet">

  <section class="card card--front" aria-label="Card front">
    <svg class="card__shape" viewBox="0 0 660 377" aria-hidden="true">
      <path class="leaf" d="M 60 440 Q 20 40 540 -50 Q 720 330 60 440 Z"/>
    </svg>
    <div class="brand">
      <span class="brand__badge"></span>
      <span class="brand__name">Calm Cradle</span>
    </div>
    <ul class="services">
      <li>Pre and Post Natal Yoga</li>
      <li>Pregnancy Workshops</li>
      <li>Hypnobirthing Courses</li>
    </ul>
  </section>

  <section class="card card--back" aria-label="Card back">
    <svg class="card__shape" viewBox="0 0 660 377" aria-hidden="true">
      <circle class="ghost-circle" cx="150" cy="170" r="95"/>
      <path class="leaf" d="M 160 440 Q 110 40 580 -50 Q 760 330 160 440 Z"/>
    </svg>
    <p class="holder-name">Marla Penrick</p>
    <div class="contact">
      <p>Fb- calmcradlestudiolakebay</p>
      <p>Mobile- 0482 315 746</p>
    </div>
  </section>

</main>
</body>
</html>
```